Business Card Design for a Handbags business

We are modernising our handbags website (see attached file for new front page) and are in need of a modern business card and a related design we can use on a small marquee at the markets, on letterhead, emails etc.

As the leather handbags we mostly import are from Italy, we want a smart modern European feel to the design. We are currently thinking about changing the name of the business from Larkmoor Handbags (see www.larkmoorhandbags.com.au) to Vintessa Handbags. Also open to other suggestions you may have that communicates the European influence and quality.

Target Market(s)

25-65 year old women (and some men)

Industry/Entity Type

Business

Contact Information for Business Card

Single or double sided - whichever creates more of an impact

Font styles to use
Serif
Sans Serif

Requirements
Must have
• Clean crisp look, slightly Italian or European look and feel to reflect where the handbags are imported from
Nice to have
• open to ideas

```html
<!DOCTYPE html>
<html lang="en">
<head>
<meta charset="utf-8">
<title>Vintessa Handbags – Business Card</title>
<link rel="stylesheet" href="https://fonts.googleapis.com/css2?family=Source+Sans+3:wght@400;600;700&display=swap">
<style>
  :root {
    --backdrop: #a3a3a3;
    --card: #221b1c;
    --ink: #ffffff;
    --ink-soft: #f2f2f2;
  }
  html, body {
    margin: 0;
    padding: 0;
    width: 1200px;
    height: 900px;
    overflow: hidden;
    background: var(--backdrop);
  }
  .canvas {
    position: relative;
    width: 1200px;
    height: 900px;
    font-family: "Source Sans 3", sans-serif;
  }
  .card {
    position: absolute;
    top: 275px;
    width: 477px;
    height: 293px;
    background: var(--card);
    color: var(--ink);
    text-align: center;
  }
  .card--back {
    left: 116px;
    border-radius: 0 60px 0 60px;
  }
  .card--front {
    left: 622px;
    border-radius: 60px 0 60px 0;
  }
  .contact {
    position: absolute;
    left: 0;
    right: 0;
    top: 84px;
    margin: 0;
    font-style: normal;
  }
  .contact__name {
    display: block;
    font-size: 18.5px;
    font-weight: 600;
    line-height: 24px;
  }
  .contact__line {
    display: block;
    font-size: 13.5px;
    line-height: 18px;
    color: var(--ink-soft);
  }
  .contact__phone { margin-top: 2px; }
  .contact__area { margin-top: 19px; }
  .contact__web { margin-top: 23px; }
  .brand {
    position: absolute;
    left: 0;
    right: 0;
    top: 92px;
  }
  .brand__name {
    display: block;
    font-size: 62px;
    font-weight: 600;
    line-height: 70px;
    letter-spacing: 1px;
  }
  .brand__tagline {
    display: block;
    margin-top: 6px;
    font-size: 18px;
    font-weight: 600;
    line-height: 22px;
    letter-spacing: 0.5px;
  }
</style>
</head>
<body>
  <main class="canvas">
    <section class="card card--back" aria-label="Business card back">
      <address class="contact">
        <span class="contact__name">Rebecca Lowe</span>
        <span class="contact__line contact__phone">0412 555 019</span>
        <span class="contact__line contact__area">Ashgrove, Brisbane</span>
        <span class="contact__line contact__web">www.larkmoorhandbags.com.au</span>
      </address>
    </section>
    <section class="card card--front" aria-label="Business card front">
      <div class="brand">
        <span class="brand__name">Vintessa</span>
        <span class="brand__tagline">Handbags &amp; Accessories</span>
      </div>
    </section>
  </main>
</body>
</html>
```